Driving School Business card design

Hi, we are starting a new business (Driving School) and would like your help with our business card design.
We are located in Adelaide SA.
Our aim is to help young people achieve best possible results by promoting safe and stress free driving.

Name of our school is "Velmira" which means best or most favorable.

Hope there is someone out there in wonderful world of design who can think outside of square and give us recognizable/ unique business card design.

Target Market(s)

16+

Industry/Entity Type

Business

Contact Information for Business Card

Name of our business is "Velmira driver training"
Our idea is to make letter "L' in Velmira more distinct (noticeable) by different color or font, so it gets associated with learner driver.
We like combination of white, dark gray and yellow but do not limit our self to that.
Reverse side of our card would have to incorporate writing space for date and time of the next lesson.

Requirements
Must have
• Business name: Velmira driver training
• Owner/ instructor name
• Mobile no:
• Chatterloop logo
Should not have
• Anything Not associated with driving

```html
<!DOCTYPE html>
<html lang="en">
<head>
<meta charset="utf-8">
<title>Velmira driver training – business card</title>
<link rel="stylesheet" href="https://fonts.googleapis.com/css2?family=Open+Sans:wght@300;400;600;700&display=swap">
<style>
  :root {
    --backdrop: #e4e2de;
    --charcoal: #333333;
    --charcoal-soft: rgba(51, 51, 51, 0.92);
    --mist: rgba(245, 245, 245, 0.78);
    --ink: #3c3c3c;
    --yellow: #f3e23b;
    --white: #ffffff;
    --pixel: #d9d9d9;
    --text-font: "Open Sans", Arial, sans-serif;
  }
  * { box-sizing: border-box; margin: 0; padding: 0; }
  html, body { width: 1200px; height: 1023px; overflow: hidden; }
  body {
    background: var(--backdrop);
    font-family: var(--text-font);
    position: relative;
  }
  .card {
    position: absolute;
    left: 290px;
    width: 620px;
    height: 378px;
    border-radius: 6px;
    overflow: hidden;
    box-shadow: 0 10px 30px rgba(0,0,0,0.18);
  }
  .card-front { top: 100px; }
  .card-back  { top: 540px; background: var(--white); }

  /* front */
  .road-photo {
    position: absolute; inset: 0;
    background:
      linear-gradient(180deg, rgba(40,40,40,0.75) 0%, rgba(160,160,160,0.2) 45%, rgba(60,60,60,0.7) 100%),
      linear-gradient(90deg, #5a5a5a 0%, #b9b9b9 45%, #7d7d7d 70%, #2e2e2e 100%);
  }
  .info-panel {
    position: absolute;
    left: 22px; top: 86px;
    width: 360px; height: 270px;
    background: var(--mist);
    border-radius: 14px;
  }
  .icon-rail {
    position: absolute;
    left: 22px; top: 86px;
    width: 58px; height: 270px;
    background: var(--charcoal-soft);
    border-radius: 14px;
  }
  .icon-rail svg {
    position: absolute; left: 17px;
    width: 24px; height: 24px;
  }
  .contact-line {
    position: absolute; left: 100px;
    color: var(--ink);
    font-weight: 300;
    white-space: nowrap;
  }
  .contact-name { top: 110px; font-size: 30px; }
  .contact-name .role { font-size: 15px; font-weight: 400; letter-spacing: 0.5px; text-transform: uppercase; }
  .contact-phone { top: 176px; font-size: 17px; }
  .contact-email { top: 238px; font-size: 17px; }
  .contact-social { top: 300px; font-size: 17px; }

  .brand-panel {
    position: absolute;
    right: 22px; top: 22px;
    width: 220px; height: 250px;
    background: var(--charcoal);
    border-radius: 16px;
    display: flex; flex-direction: column;
    align-items: center; justify-content: center;
    gap: 14px;
  }
  .brand-square {
    width: 30px; height: 30px;
    background: var(--yellow);
  }
  .brand-name {
    color: var(--yellow);
    font-weight: 700;
    font-size: 22px;
    text-align: center;
    line-height: 1.2;
    text-transform: uppercase;
  }

  /* back */
  .pixel-fade {
    position: absolute; right: 0; top: 0;
    width: 300px; height: 378px;
    background: linear-gradient(90deg, rgba(255,255,255,1) 0%, var(--pixel) 100%);
    opacity: 0.6;
  }
  .lesson-box {
    position: absolute;
    left: 26px; top: 30px;
    width: 270px; height: 150px;
    background: var(--charcoal);
    border-radius: 14px;
    padding: 20px 24px;
    color: var(--white);
  }
  .lesson-heading { font-size: 14px; font-weight: 600; letter-spacing: 0.5px; text-transform: uppercase; color: var(--yellow); }
  .lesson-row {
    display: flex; align-items: flex-end; gap: 12px;
    margin-top: 18px;
  }
  .lesson-label { font-size: 18px; font-weight: 400; width: 48px; line-height: 1; }
  .lesson-line {
    flex: 1;
    height: 1px; background: rgba(255,255,255,0.6);
  }
  .back-brand {
    position: absolute;
    right: 40px; bottom: 50px;
    display: flex; align-items: center; gap: 16px;
  }
  .back-brand .brand-square { width: 44px; height: 44px; background: var(--charcoal); }
  .back-brand .brand-name { color: var(--charcoal); font-size: 30px; text-align: left; }
</style>
</head>
<body>
  <section class="card card-front">
    <div class="road-photo" role="img" aria-label="Black and white photo of a country road lined with trees"></div>
    <div class="info-panel"></div>
    <div class="icon-rail">
      <svg style="top:20px" viewBox="0 0 24 24" aria-hidden="true"><circle cx="12" cy="7" r="5" fill="var(--yellow)"/><path d="M3 23c0-6 4-9 9-9s9 3 9 9z" fill="var(--yellow)"/></svg>
      <svg style="top:86px" viewBox="0 0 24 24" aria-hidden="true"><path d="M6 2l4 4-2 3c1 3 4 6 7 7l3-2 4 4-3 4C11 22 2 13 2 5z" fill="var(--yellow)"/></svg>
      <svg style="top:148px" viewBox="0 0 24 24" aria-hidden="true"><rect x="1" y="5" width="22" height="15" rx="1" fill="var(--yellow)"/><path d="M2 6l10 8 10-8" fill="none" stroke="var(--charcoal)" stroke-width="1.6"/></svg>
      <svg style="top:210px" viewBox="0 0 24 24" aria-hidden="true"><circle cx="12" cy="12" r="10" fill="var(--yellow)"/></svg>
    </div>
    <p class="contact-line contact-name">Jordan Vale/<span class="role">Director</span></p>
    <p class="contact-line contact-phone">0412 555 019</p>
    <p class="contact-line contact-email">lessons@velmira-drive.com</p>
    <p class="contact-line contact-social">VelmiraDriverTraining</p>
    <div class="brand-panel">
      <span class="brand-square"></span>
      <p class="brand-name">Velmira<br>driver training</p>
    </div>
  </section>

  <section class="card card-back">
    <div class="pixel-fade"></div>
    <div class="lesson-box">
      <p class="lesson-heading">Next lesson</p>
      <div class="lesson-row"><span class="lesson-label">Date</span><span class="lesson-line"></span></div>
      <div class="lesson-row"><span class="lesson-label">Time</span><span class="lesson-line"></span></div>
    </div>
    <div class="back-brand">
      <span class="brand-square"></span>
      <p class="brand-name">Velmira<br>driver training</p>
    </div>
  </section>
</body>
</html>
```